MOSLEN Environmental needs an upgrade to its current business cards design

We need an upgrade to our current business cards design, where the MOSLEN acronym is included, as possible and not being overloaded.
MOSLEN Environmental is an Environmental Consultancy Firm based in Sydney.
We would like to see creative designs different from the standard type of business cards (for example, rounded edges, different to standard size of common business cards.

Target Market(s)

industrial companies (oil & gas, petrochemical, mining, insolvency, finance and manufacturing), developers, architect firms, law firms.

Industry/Entity Type

Business

Contact Information for Business Card

logos (brand and acronym), if they don't appear overloaded.
name
role
name of company (MOSLEN Environmental),
address (Level 3, Suite 3C, 47-49 Dorrigan Lane, Wexmoor, NSW, 2188) landline (02 7314 2986)
mobile (staff member)
email (staff member) and
website (www.moslengreen.example).
Include: Contaminated Land, Site Remediation, Groundwater Assessment, Health and Ecological Risk Assessments, Acid Sulfate Soils, Waste Classification.

Font styles to use
Serif
Sans Serif

Requirements
Must have
• A creative design different to the standard type of business cards.
Nice to have
• Rounded edges
• Different size of business cards rather than the standard size.
Should not have
• Preferable not to use white colour background, unless it is required from a creative design proposed.
• Not an overloaded design.
• Avoid black colours

```html
<!DOCTYPE html>
<html lang="en">
<head>
<meta charset="utf-8">
<title>MOSLEN Environmental business cards</title>
<link rel="stylesheet" href="https://fonts.googleapis.com/css2?family=Montserrat:wght@300;400;500;700&display=swap">
<style>
  :root {
    --stage: #d2d3d5;
    --card: #404040;
    --card-shadow: rgba(0, 0, 0, 0.35);
    --green: #6db33f;
    --logo-green: #8dc63f;
    --text-light: #f2f2f2;
    --mark-faint: #393939;
  }
  * { margin: 0; padding: 0; box-sizing: border-box; }
  html, body {
    width: 1200px;
    height: 927px;
    overflow: hidden;
    background: var(--stage);
    font-family: "Montserrat", sans-serif;
  }
  .stage { position: relative; width: 1200px; height: 927px; }
  .card {
    position: absolute;
    top: 87px;
    width: 430px;
    height: 752px;
    border-radius: 32px;
    background: var(--card);
    box-shadow: 6px 8px 12px var(--card-shadow);
    color: var(--text-light);
    text-align: center;
    overflow: hidden;
  }
  .card--front { left: 145px; }
  .card--back { left: 625px; }

  .card > * { position: absolute; left: 0; width: 100%; }

  .brand__name {
    font-size: 78px;
    line-height: 78px;
    font-weight: 700;
    letter-spacing: 1px;
  }
  .brand__sub {
    font-size: 28px;
    line-height: 28px;
    font-weight: 700;
    letter-spacing: 6px;
    padding-left: 6px;
  }
  .card--front .brand__name { top: 70px; color: var(--logo-green); }
  .card--front .brand__sub { top: 165px; color: var(--logo-green); }
  .card--back .brand__name { top: 219px; color: var(--mark-faint); }
  .card--back .brand__sub { top: 311px; color: var(--mark-faint); }

  .person__name {
    top: 446px;
    font-size: 28px;
    line-height: 34px;
    font-weight: 500;
    letter-spacing: 1px;
    color: var(--green);
  }
  .person__role,
  .address,
  .contact,
  .services {
    font-size: 19px;
    font-weight: 300;
    line-height: 23.2px;
    letter-spacing: 0.3px;
  }
  .person__role { top: 480px; }
  .address { top: 515px; }
  .contact-icons {
    top: 598px;
    display: flex;
    justify-content: center;
    gap: 8px;
    height: 14px;
  }
  .contact-icons svg { width: 14px; height: 14px; }
  .contact { top: 624px; }
  .contact__highlight { color: var(--green); font-weight: 400; }

  .services { top: 396px; list-style: none; }
</style>
</head>
<body>
<main class="stage">

  <section class="card card--front" aria-label="Business card front">
    <span class="brand__name">MOSLEN</span>
    <span class="brand__sub">ENVIRONMENTAL</span>

    <h1 class="person__name">ROWAN KELLER</h1>
    <p class="person__role">Project Engineer</p>
    <p class="address">Level 3, Suite 3C<br>47-49 Dorrigan Lane<br>Wexmoor, NSW, 2188</p>

    <div class="contact-icons" aria-hidden="true">
      <svg viewBox="0 0 16 16" fill="none" stroke="#6db33f" stroke-width="1.6" stroke-linejoin="round">
        <path d="M4 1.5 L6.5 4.5 L5 6.5 C6 9 7.5 10.5 9.5 11.5 L11.5 10 L14.5 12.5 L12.5 14.5 C7 14 2 9 1.5 3.5 Z"/>
      </svg>
      <svg viewBox="0 0 16 16" fill="none" stroke="#6db33f" stroke-width="1.5">
        <rect x="1.5" y="3.5" width="13" height="9" rx="1"/>
        <path d="M1.5 4 L8 9 L14.5 4"/>
      </svg>
      <svg viewBox="0 0 16 16" fill="none" stroke="#6db33f" stroke-width="1.2">
        <circle cx="8" cy="8" r="6.5"/>
        <ellipse cx="8" cy="8" rx="3" ry="6.5"/>
        <path d="M1.5 8 H14.5 M2.6 4.5 H13.4 M2.6 11.5 H13.4"/>
      </svg>
    </div>

    <p class="contact">
      (02 7314 2986)<br>
      rowan@moslengreen.example<br>
      www.<span class="contact__highlight">moslengreen</span>.example
    </p>
  </section>

  <section class="card card--back" aria-label="Business card back">
    <span class="brand__name" aria-hidden="true">MOSLEN</span>
    <span class="brand__sub" aria-hidden="true">ENVIRONMENTAL</span>

    <ul class="services">
      <li>Contaminated Land</li>
      <li>Site Remediation</li>
      <li>Groundwater Assessment</li>
      <li>Health and Ecological Risk Assessments</li>
      <li>Acid Sulfate Soils</li>
      <li>Waste Classification</li>
    </ul>
  </section>

</main>
</body>
</html>
```